New Billboard Design Project

I would like a billboard with the attached image of me Vectored onto it. With my name Marcus Thornley

also the attached logo

Maybe saying "WELCOME TO BRIGHTMEADOW" large across the top.

Real Estate Professional

1.75% FULL listing service

Call/Text 410-937-2815

(Then the text below much smaller because it is required by law)

Office: 833-555-2947
2741 W Harrowgate Rd
Larkspur, MD 21099
www.brightmeadowhomes.com

Billboard size is:

48 FT X 14 FT

```html
<!DOCTYPE html>
<html lang="en">
<head>
<meta charset="utf-8">
<title>Brightmeadow Billboard</title>
<link href="https://fonts.googleapis.com/css2?family=Cinzel:wght@400;600&family=Allura&display=swap" rel="stylesheet">
<style>
  :root {
    --navy: #0c2450;
    --navy-deep: #081a3c;
    --paper: #f4f4f4;
    --paper-shade: #d9d9d9;
    --silver: #a9a9ab;
    --pill-light: #f7f7f7;
    --pill-dark: #bdbdc0;
    --ink-white: #ffffff;
    --stage: #dcdcdc;
  }
  html, body {
    margin: 0;
    width: 1192px;
    height: 1200px;
    overflow: hidden;
    background: var(--stage);
  }
  .canvas {
    width: 1192px;
    height: 1200px;
    display: flex;
    align-items: center;
    justify-content: center;
  }
  .billboard {
    width: 1120px;
    height: 326px;
    display: block;
    box-shadow: 0 2px 8px rgba(0,0,0,0.12);
  }
  .serif { font-family: "Cinzel", "Times New Roman", serif; }
  .script { font-family: "Allura", cursive; }
</style>
</head>
<body>
<main class="canvas">
  <svg class="billboard" viewBox="0 0 1650 480" xmlns="http://www.w3.org/2000/svg" aria-label="Billboard for Marcus Thornley, real estate professional">
    <defs>
      <radialGradient id="paper-texture" cx="50%" cy="45%" r="75%">
        <stop offset="0" stop-color="var(--paper)"/>
        <stop offset="0.7" stop-color="#ebebeb"/>
        <stop offset="1" stop-color="var(--paper-shade)"/>
      </radialGradient>
      <linearGradient id="pill-fill" x1="0" y1="0" x2="0" y2="1">
        <stop offset="0" stop-color="var(--pill-light)"/>
        <stop offset="1" stop-color="var(--pill-dark)"/>
      </linearGradient>
      <linearGradient id="portrait-tones" x1="0" y1="0" x2="0" y2="1">
        <stop offset="0" stop-color="#c89a82"/>
        <stop offset="0.3" stop-color="#b98872"/>
        <stop offset="0.4" stop-color="#2a3550"/>
        <stop offset="1" stop-color="#1d2740"/>
      </linearGradient>
    </defs>

    <rect class="panel" width="1650" height="480" fill="url(#paper-texture)"/>

    <path class="crescent" d="M505 60 Q395 250 525 480 L545 480 Q430 260 520 55 Z" fill="var(--navy)"/>

    <path class="silver-arc" d="M1195 0 L1245 0 Q1360 230 1240 480 L1190 480 Q1300 240 1195 0 Z" fill="var(--silver)"/>

    <path class="centre-field" d="M540 0 L1205 0 Q1315 240 1200 480 L540 480 Q440 240 540 0 Z" fill="var(--navy)"/>

    <g class="brand">
      <circle cx="212" cy="120" r="58" fill="none" stroke="var(--navy)" stroke-width="4"/>
      <text class="serif brand-small" x="212" y="230" text-anchor="middle" font-size="15" letter-spacing="8" fill="var(--navy)">THE</text>
      <text class="serif brand-name" x="212" y="270" text-anchor="middle" font-size="31" fill="var(--navy)">BRIGHTMEADOW TEAM</text>
      <text class="serif brand-small" x="212" y="293" text-anchor="middle" font-size="12" letter-spacing="2" fill="var(--navy)">AT KEYSTONE REAL ESTATE</text>
      <line x1="40" y1="224" x2="150" y2="224" stroke="var(--navy)" stroke-width="1.5"/>
      <line x1="274" y1="224" x2="384" y2="224" stroke="var(--navy)" stroke-width="1.5"/>
    </g>

    <g class="contact serif" fill="var(--navy-deep)" text-anchor="middle" font-size="21">
      <text x="212" y="352">Office: 833-555-2947</text>
      <text x="212" y="378">2741 W Harrowgate Rd</text>
      <text x="212" y="404">Larkspur, MD 21099</text>
      <text x="212" y="431" font-weight="600" font-size="19">www.brightmeadowhomes.com</text>
    </g>

    <g class="headline" fill="var(--ink-white)">
      <text class="script" x="552" y="100" font-size="58">Welcome to</text>
      <text class="serif" x="792" y="92" font-size="48" textLength="408" lengthAdjust="spacingAndGlyphs">BRIGHTMEADOW</text>
      <line x1="792" y1="128" x2="953" y2="128" stroke="var(--ink-white)" stroke-width="1.5"/>
      <rect x="860" y="125" width="30" height="6" fill="var(--ink-white)"/>
    </g>

    <g class="agent serif" fill="var(--ink-white)" text-anchor="middle">
      <text x="872" y="196" font-size="30" letter-spacing="1">— Real Estate Professional —</text>
      <text x="872" y="272" font-size="68" font-weight="600">Marcus Thornley</text>
      <text x="872" y="345" font-size="28" letter-spacing="1">1.75% FULL listing service</text>
    </g>

    <g class="call-pill">
      <rect x="546" y="364" width="654" height="72" rx="36" fill="url(#pill-fill)"/>
      <text class="serif" x="873" y="417" text-anchor="middle" font-size="46" fill="var(--navy)">Call/Text 410-937-2815</text>
    </g>

    <g class="portrait" role="img" aria-label="Cut-out photo of the agent in a navy suit jacket and striped shirt">
      <path d="M1265 480 L1280 300 Q1300 165 1420 150 Q1380 120 1375 70 Q1380 20 1435 18 Q1490 20 1490 80 Q1488 125 1460 150 Q1590 170 1605 300 L1615 480 Z" fill="url(#portrait-tones)"/>
    </g>
  </svg>
</main>
</body>
</html>
```